Shop front signage design for Bubble Tea Shop

Tapioca Grove is Sydney based Green Tea Shop.We are looking for a modern and sleek signage for shop front end. We have Aluminium Composite Panel and Awning sign at the shop front. We will keep Aluminium composite panel simple with logo and text. We are after awning design which is above glass door and under the panel. Old Awning is PVC foam in two pieces 2310mm w x 1000mm h. We need someone to design awing. It should reflect Bubble tea and using bubble tea cups with pearls is essential. Stock images can be used. Avoid using icons or illustrative icons as we are after real images of bubble tea cup. This is to ensure that the brand is not taken as juice shop or cafe.
Panel Dimensions is 5250 mm w x 580 mm h.Awning/ Fascia sign is 4720 mm w x 1000 mm h.
Logo and signage concept is attached.

Target Market(s)

Corporate Male and Female, school, general public.

Colors
f36e22
333333
000000
eaeaea
cbcbcb

Requirements
Must have
• Bubble tea cups with fruit or milk tea.
Should not have
• Icons, illustration

```html
<!DOCTYPE html>
<html lang="en">
<head>
<meta charset="utf-8">
<title>Tapioca Grove – Shop Front Signage</title>
<link rel="stylesheet" href="https://fonts.googleapis.com/css2?family=Arimo:wght@700&family=Open+Sans:wght@400&display=swap">
<style>
  :root {
    --board-bg: #232323;
    --sign-bg: #ffffff;
    --ink: #000000;
    --tea-green: #3f8a2a;
    --label: #ffffff;
    --fruit-pink: #e3a6b8;
    --fruit-orange: #f39a3c;
    --fruit-lime: #c7d46a;
    --milk-tea: #dccab4;
    --milk-tea-light: #f1e9df;
  }
  * { margin: 0; padding: 0; box-sizing: border-box; }
  html, body { width: 1200px; height: 1200px; overflow: hidden; }
  body {
    background: var(--board-bg);
    position: relative;
    font-family: "Arimo", Arial, sans-serif;
  }
  .sign {
    position: absolute;
    background: var(--sign-bg);
    box-shadow: 0 8px 18px rgba(0,0,0,0.45);
    overflow: hidden;
  }
  .awning { left: 62px; top: 322px; width: 1066px; height: 225px; }
  .panel  { left: 62px; top: 762px; width: 1059px; height: 117px; }

  .photo { position: absolute; }
  .photo--fruit-cups {
    left: 66px; top: 8px; width: 176px; height: 217px;
    background: linear-gradient(90deg, var(--fruit-pink) 0%, var(--fruit-orange) 45%, var(--fruit-orange) 62%, var(--fruit-lime) 100%);
    border-radius: 40px 40px 12px 12px;
    opacity: 0.85;
  }
  .photo--milk-tea {
    left: 882px; top: 6px; width: 184px; height: 219px;
    background: linear-gradient(180deg, var(--milk-tea-light) 0%, var(--milk-tea) 60%, #cdb79c 100%);
    border-radius: 20px 0 0 0;
  }

  .brand {
    position: absolute;
    display: flex;
    align-items: center;
    color: var(--ink);
    font-weight: 700;
    white-space: nowrap;
  }
  .brand__dot {
    border: 4px solid var(--ink);
    border-radius: 50%;
    flex: none;
  }
  .awning .brand { left: 378px; top: 62px; font-size: 36px; gap: 14px; }
  .awning .brand__dot { width: 64px; height: 64px; }

  .tagline-box {
    position: absolute;
    left: 336px; top: 149px; width: 438px; height: 47px;
    background: var(--tea-green);
    color: #fff;
    font-size: 39px;
    line-height: 47px;
    text-align: center;
    letter-spacing: 0.5px;
  }

  .panel .brand { top: 0; height: 117px; font-size: 25px; gap: 10px; }
  .panel .brand__dot { width: 44px; height: 44px; border-width: 3px; }
  .panel .brand--left { left: 50px; }
  .panel .brand--right { left: 762px; }
  .panel-tagline {
    position: absolute;
    left: 0; right: 0; top: 0;
    line-height: 117px;
    text-align: center;
    color: var(--tea-green);
    font-size: 35px;
    letter-spacing: 0.5px;
    padding-right: 36px;
  }

  .sign-label {
    position: absolute;
    left: 0; width: 1160px;
    text-align: center;
    font-family: "Open Sans", Arial, sans-serif;
    font-weight: 400;
    color: var(--label);
    font-size: 34px;
  }
  .sign-label--awning { top: 606px; }
  .sign-label--panel { top: 916px; width: 1120px; }
</style>
</head>
<body>
  <section class="sign awning">
    <div class="photo photo--fruit-cups" role="img" aria-label="Photo of three bubble tea cups with fruit tea and tapioca pearls, domed lids and straws"></div>
    <div class="brand">
      <span class="brand__dot"></span>
      <span class="brand__name">Tapioca Grove</span>
    </div>
    <div class="tagline-box">A GREEN TEA SHOP</div>
    <div class="photo photo--milk-tea" role="img" aria-label="Photo of a hand holding a milk tea cup with tapioca pearls and a black straw"></div>
  </section>
  <p class="sign-label sign-label--awning">AWNING/ FASCIA SIGN</p>

  <section class="sign panel">
    <div class="brand brand--left">
      <span class="brand__dot"></span>
      <span class="brand__name">Tapioca Grove</span>
    </div>
    <div class="panel-tagline">A GREEN TEA SHOP</div>
    <div class="brand brand--right">
      <span class="brand__dot"></span>
      <span class="brand__name">Tapioca Grove</span>
    </div>
  </section>
  <p class="sign-label sign-label--panel">PANEL DESIGN</p>
</body>
</html>
```